Meridian Swift add on sales tool2017

This will be a flyer to leave with our clients we just did work for. We want to entice them to use our other services over the next 30 days with a discount, money off etc. we will write in the special and the expiration date. I want the client to read the description and see a picture of the service they may want done.

Target Market(s)

Repeat clients

Industry/Entity Type

Cleaning Service

Font styles to use
Serif
Sans Serif

Colors
ec1f27
000000
b1b1b1

Requirements
Must have
• Call to action! look high end market, clients show we do 1st class work.
• Don't Waite
Nice to have
• Classy, quality, I'm open to using other pictures that may look better
Should not have
• Look like a typical carpet cleaners special flyer
• Not to look cluttered

```html
<!DOCTYPE html>
<html lang="en">
<head>
<meta charset="utf-8">
<title>Meridian Swift – 30 Day Special Offer Flyer</title>
<link rel="stylesheet" href="https://fonts.googleapis.com/css2?family=Anton&family=Oswald:wght@500&family=Questrial&family=Roboto:wght@400;700&display=swap">
<style>
  :root{
    --red:#ec1f27;
    --black:#000000;
    --ink:#1c1c1c;
    --grey:#b1b1b1;
    --light:#dcdcdc;
    --white:#ffffff;
    --page:#e9e9e9;
  }
  *{box-sizing:border-box;margin:0;padding:0}
  html,body{width:1200px;height:1200px;overflow:hidden;background:var(--page)}
  .flyer{
    position:absolute;left:185px;top:17px;width:830px;height:1166px;
    background:var(--ink);overflow:hidden;
    font-family:"Roboto",Arial,sans-serif;color:var(--white);
    box-shadow:0 4px 18px rgba(0,0,0,.25);
  }
  .hero-photo{
    position:absolute;left:0;top:0;width:830px;height:440px;
    background:linear-gradient(180deg,#f2efea 0%,#e6e3dd 45%,#cfd8cf 75%,#4f9a5f 100%);
  }
  .wave{position:absolute;left:0;top:0}
  .badge{position:absolute;left:539px;top:301px;width:270px;height:270px;text-align:center}
  .badge svg{position:absolute;left:0;top:0}
  .badge-days{position:absolute;left:0;right:0;top:64px;font-family:"Anton",Impact,sans-serif;font-size:62px;line-height:1;color:var(--red);letter-spacing:1px}
  .badge-offer{position:absolute;left:0;right:0;top:137px;font-family:"Anton",Impact,sans-serif;font-size:28px;line-height:1;color:var(--black);letter-spacing:.5px}
  .badge-cta{position:absolute;left:0;right:0;top:183px;font-family:"Roboto",Arial,sans-serif;font-weight:700;font-size:17px;color:var(--red)}
  .brand{position:absolute;left:52px;top:440px;width:340px;text-align:center}
  .brand-name{font-family:"Questrial",sans-serif;font-size:36px;color:var(--light);letter-spacing:1px;line-height:1}
  .headline{position:absolute;left:0;right:0;top:585px;text-align:center}
  .headline-top{font-family:"Questrial",sans-serif;font-size:55px;color:var(--red);line-height:1;letter-spacing:1px}
  .headline-main{font-family:"Oswald",sans-serif;font-weight:500;font-size:78px;color:var(--light);line-height:1;margin-top:6px;letter-spacing:-1.5px}
  .service{position:absolute;width:370px;height:120px}
  .service-photo{position:absolute;left:0;top:0;width:130px;height:100px;border:4px solid var(--white)}
  .service-label{
    position:absolute;left:126px;top:5px;background:var(--white);
    border-radius:0 14px 14px 0;padding:5px 12px 5px 14px;
    font-size:14.5px;line-height:17px;color:#8a8a8a;white-space:nowrap;
  }
  .service-label b{color:var(--red);font-weight:700}
  .service-text{position:absolute;left:144px;width:200px;font-size:11.8px;line-height:14px;color:var(--white);text-align:justify}
  .contact{
    position:absolute;left:432px;top:1018px;width:349px;height:113px;
    border:2px solid var(--white);border-radius:20px;font-size:13px;line-height:16px;
  }
  .contact-address{position:absolute;left:14px;top:22px;display:flex;gap:4px}
  .contact-phone{position:absolute;left:232px;top:22px;display:flex;gap:5px}
  .contact-expiry{position:absolute;left:11px;right:6px;top:77px;display:flex;gap:6px;align-items:flex-end}
  .contact-expiry span.line{flex:1;border-bottom:1px dotted var(--white);height:12px}
  .footer-rule{position:absolute;left:0;right:0;top:1154px;height:2px;background:#555}
  .footer-bar{position:absolute;left:0;right:0;top:1158px;height:8px;background:var(--red)}
</style>
</head>
<body>
<main class="flyer">
  <div class="hero-photo" role="img" aria-label="Photo of a smiling three-person cleaning team in green aprons in a bright kitchen, one holding a yellow spray bottle"></div>

  <svg class="wave" width="830" height="1166" viewBox="0 0 830 1166" aria-hidden="true">
    <path d="M0,236 C170,205 330,225 480,330 S720,440 830,405 L830,1166 L0,1166 Z" fill="#e01c24"/>
    <path d="M0,252 C170,222 330,245 470,345 S720,455 830,422 L830,1166 L0,1166 Z" fill="#111"/>
    <path d="M0,262 C170,240 330,262 460,360 S720,470 830,432 L830,1166 L0,1166 Z" fill="#ffffff"/>
    <path d="M0,272 C170,258 330,282 450,380 S720,485 830,440 L830,1166 L0,1166 Z" fill="#1c1c1c"/>
  </svg>

  <div class="badge">
    <svg width="270" height="270" viewBox="0 0 270 270" aria-hidden="true">
      <circle cx="135" cy="135" r="133" fill="#ffffff"/>
      <circle cx="135" cy="135" r="126" fill="#111"/>
      <circle cx="135" cy="135" r="119" fill="#ec1f27"/>
      <circle cx="135" cy="135" r="112" fill="#ffffff"/>
    </svg>
    <div class="badge-days">30 DAY</div>
    <div class="badge-offer">SPECIAL OFFER!</div>
    <div class="badge-cta">Call Now to Book</div>
  </div>

  <div class="brand">
    <div class="brand-name">MERIDIAN SWIFT</div>
  </div>

  <header class="headline">
    <div class="headline-top">ONE STOP FOR ALL YOUR</div>
    <div class="headline-main">HOME CLEANING NEEDS</div>
  </header>

  <section class="service" style="left:52px;top:763px">
    <div class="service-photo" role="img" aria-label="Photo of a freshly cleaned carpeted staircase" style="background:linear-gradient(160deg,#c9c2b8,#8d8478)"></div>
    <div class="service-label"><b>CARPET</b> CLEANING</div>
    <p class="service-text" style="top:50px">Don't let dirty carpets spoil the look of your beautiful home! With 37 years of cleaning carpets experience you can expect your carpets to look like new in most cases.</p>
  </section>

  <section class="service" style="left:52px;top:891px">
    <div class="service-photo" role="img" aria-label="Before and after photo of an upholstered chair" style="background:linear-gradient(90deg,#9aa39a,#cdd3cc 50%,#8a7a6a)"></div>
    <div class="service-label"><b>UPHOLSTERY</b> CLEANING</div>
    <p class="service-text" style="top:48px">Every day use leaves your sofa's and chairs looking dingy and can smell like dog. Our Dry cleaning, Shampoo or Rinse extraction will leave the fabric feel like clean sheet!</p>
  </section>

  <section class="service" style="left:52px;top:1021px">
    <div class="service-photo" role="img" aria-label="Photo of a technician cleaning drapes at a window" style="background:linear-gradient(135deg,#6e5a4e,#cfc8c0)"></div>
    <div class="service-label"><b>DARAPERY</b> CLEANING</div>
    <p class="service-text" style="top:46px">Drapery's act like a filter attracting atmospheric soil! Making them look dingy, We make it easy to Dry clean in-home! Safe and effective beautiful drapery again.</p>
  </section>

  <section class="service" style="left:432px;top:765px">
    <div class="service-photo" role="img" aria-label="Before and after photo of cleaned tile and grout" style="background:linear-gradient(135deg,#7a7672,#a9a49c)"></div>
    <div class="service-label"><b>TILE &amp; GROUT</b> CLEANING</div>
    <p class="service-text" style="top:41px">Tile &amp; Grout get neglected! Dirty grout can leave permanent staining. Let our professionals bring back the look of a new floor.</p>
  </section>

  <section class="service" style="left:432px;top:890px">
    <div class="service-photo" role="img" aria-label="Photo of a polished natural stone floor" style="background:linear-gradient(180deg,#6a6a66,#3e3e3a)"></div>
    <div class="service-label" style="top:6px;padding-right:12px"><b>NATURAL STONE CLEANING</b><br>&amp; POLOSHING</div>
    <p class="service-text" style="top:59px">A dull stained Marble - Granite-Travertine and other Natural stone can be revitalized to look NEW again!</p>
  </section>

  <div class="contact">
    <div class="contact-address">
      <svg width="14" height="16" viewBox="0 0 14 16" aria-hidden="true"><path d="M7 0C3.7 0 1.2 2.5 1.2 5.6 1.2 9.6 7 16 7 16s5.8-6.4 5.8-10.4C12.8 2.5 10.3 0 7 0zm0 8a2.4 2.4 0 1 1 0-4.8A2.4 2.4 0 0 1 7 8z" fill="#ec1f27"/></svg>
      <span>2214 S. Maple Dr. Suite B<br>Las Vegas</span>
    </div>
    <div class="contact-phone">
      <svg width="16" height="16" viewBox="0 0 16 16" aria-hidden="true"><path d="M3.3 0.6l2.3 2.9c.4.5.3 1.2-.1 1.6L4.3 6.2c.9 2 3.2 4.3 5.3 5.3l1.1-1.2c.4-.4 1.1-.5 1.6-.1l2.9 2.3c.5.4.6 1.1.2 1.6l-1.2 1.4c-.6.6-1.5.8-2.3.5C6.8 14.3 1.7 9.2.0 4.1c-.3-.8 0-1.7.6-2.3L2 .5c.4-.4 1-.4 1.3.1z" fill="#ec1f27"/></svg>
      <span>702 555-0147</span>
    </div>
    <div class="contact-expiry"><span>Expires :-</span><span class="line"></span></div>
  </div>

  <div class="footer-rule"></div>
  <div class="footer-bar"></div>
</main>
</body>
</html>
```